Dalton & Vesh Periodontics and Implant Solutions Business Card

We are a specialty dental practice- implants and periodontal surgery. We have just re-designed our logo and are building a new office and would like to re-design our business card. We are looking for something professional with a creative and artsy twist- something to stand out among the rest! Happy Designing!

I have uploaded all versions of our new logo and our current business card. We have 3 locations and 2 doctors.
Updates

Target Market(s)

55+

Industry/Entity Type

Dental

Contact Information for Business Card

Needs Names, logo, locations- professional and artsy!

Colors
0555a3
0592cd
34a7d7
3277b5
85cae6
85acd3
cee9f5
ecf7fb

Requirements
Must have
• our names:
• Gavin T. Dalton D.M.D.
• Marla P. Vesh D.M.D.
• Diplomate of the National Council of Gum Surgery
• Address locations:
• 462 N. Larkspur Avenue Suite 210B Plantation, FL 33324
• Tel: 954-603-2281 Fax: 954-603-2895
• 5174 Hollins Lane #C-3 Boca Raton, FL 33434
• Tel: 561-327-6018 Fax: 561-327-6092
• 381 Northwest 7th Street #412 Miami FL 33131
• Tel: 786-540-3316 Fax: 786-540-3389
Nice to have
• unique look
Should not have
• doesn't need QR like our current card has.

```html
<!DOCTYPE html>
<html lang="en">
<head>
<meta charset="utf-8">
<title>Dalton &amp; Vesh Periodontics and Implant Solutions – Business Card</title>
<link href="https://fonts.googleapis.com/css2?family=PT+Sans:wght@400;700&display=swap" rel="stylesheet">
<style>
  :root {
    --backdrop: #e4e5e7;
    --card-white: #ffffff;
    --card-blue: #223f8c;
    --navy: #1f3a8a;
    --grey-text: #7b7b7b;
    --on-blue: #ffffff;
    --faint-ring: rgba(255,255,255,0.07);
  }
  * { margin: 0; padding: 0; box-sizing: border-box; }
  html, body {
    width: 1200px; height: 900px; overflow: hidden;
    background: var(--backdrop);
    font-family: "PT Sans", "Myriad Pro", Arial, sans-serif;
  }
  .stage { position: relative; width: 1200px; height: 900px; }

  .card {
    position: absolute;
    width: 560px; height: 320px;
    border-radius: 4px;
    box-shadow: 0 6px 18px rgba(0,0,0,0.15);
    overflow: hidden;
  }

  /* Back of card */
  .card--back {
    left: 590px; top: 110px;
    background: var(--card-blue);
    color: var(--on-blue);
  }
  .card--back .backdrop-ring {
    position: absolute; left: 50%; top: 50%;
    width: 250px; height: 250px;
    transform: translate(-50%, -50%);
    border: 14px solid var(--faint-ring);
    border-radius: 50%;
  }
  .locations {
    position: absolute; left: 40px; right: 30px; top: 48px;
    font-size: 15px; line-height: 1.3;
  }
  .location { margin-bottom: 14px; }
  .location__phones { display: flex; gap: 60px; padding-left: 10px; }
  .location__phones b { font-weight: 700; margin-right: 6px; }

  /* Front of card */
  .card--front {
    left: 50px; top: 470px;
    background: var(--card-white);
  }
  .brand {
    position: absolute; left: 46px; top: 40px;
    display: flex; align-items: center; gap: 16px;
  }
  .brand__mark {
    width: 70px; height: 70px;
    border: 5px solid var(--navy);
    border-radius: 50%;
  }
  .brand__name {
    color: var(--navy);
    font-weight: 400;
    font-size: 30px;
    line-height: 1.05;
    letter-spacing: 0.5px;
  }
  .brand__name span { display: block; font-size: 16px; }

  .doctors {
    position: absolute; left: 160px; top: 160px;
  }
  .doctors__name {
    color: var(--navy); font-weight: 700; font-size: 20px;
    text-transform: uppercase; line-height: 1.2;
  }
  .doctors__credential {
    color: var(--grey-text); font-size: 17px; margin-top: 2px;
  }
  .contact {
    position: absolute; left: 205px; top: 250px;
    font-size: 17px; line-height: 1.3;
    color: var(--grey-text);
  }
  .contact b { color: var(--navy); font-weight: 700; margin-right: 8px; }
</style>
</head>
<body>
<div class="stage">

  <section class="card card--back" aria-label="Back of business card">
    <div class="backdrop-ring"></div>
    <div class="locations">
      <div class="location">
        <div>462 N. Larkspur Avenue Suite 210B Plantation, FL 33324</div>
        <div class="location__phones"><span><b>Tel:</b>954-603-2281</span><span><b>Fax:</b>954-603-2895</span></div>
      </div>
      <div class="location">
        <div>5174 Hollins Lane #C-3 Boca Raton, FL 33434</div>
        <div class="location__phones"><span><b>Tel:</b>561-327-6018</span><span><b>Fax:</b>561-327-6092</span></div>
      </div>
      <div class="location">
        <div>381 Northwest 7th Street #412 Miami FL 33131</div>
        <div class="location__phones"><span><b>Tel:</b>786-540-3316</span><span><b>Fax:</b>786-540-3389</span></div>
      </div>
    </div>
  </section>

  <section class="card card--front" aria-label="Front of business card">
    <div class="brand">
      <div class="brand__mark"></div>
      <div class="brand__name">DALTON &amp; VESH<span>Periodontics and Implant Solutions</span></div>
    </div>
    <div class="doctors">
      <div class="doctors__name">Gavin T. Dalton D.M.D.</div>
      <div class="doctors__name">Marla P. Vesh D.M.D.</div>
      <div class="doctors__credential">Diplomate of the National Council of Gum Surgery</div>
    </div>
    <div class="contact">
      <div><b>Email:</b>contactus@daltonvesh-perio.com</div>
      <div><b>Website:</b>www.daltonvesh-perio.com</div>
    </div>
  </section>

</div>
</body>
</html>
```